Heron Freightways LLC needs a web desigh ASAP!

We need a fully functioning web site for our trucking company!
we currently have our domain and logo.
Attached you will find our logo files and word documents with info we would like to include in our web page. (Navigation Tabs and dropdown menu)
Our domain is heronfreightways.net (from webnestly)
Our Chatterbook page is Heron Freightways LLC. You can find pictures and a little bit about our company.
our original logo is the one with bull on the left side.
Our trucking company is based in south Texas, but travel within the USA and Canada.

Target Market(s)

Logistic
Refrigerated Fleet Clients
Transportation
Trucking companies

Industry/Entity Type

Trucking Company

Coding

Coded - Design and coding required

Number of Pages Required

1 page

Font styles to use
Sans Serif

Colors
f04a51
3277b5
ffffff

Requirements
Must have
• our main email contact is Info@heronfreightways.net
• we would like see the colors of our logo. it would be nice to have a truck with our logo in the background.
• We need a web site that we can manage on our own easily.
Nice to have
• roads, highways
• get a quote module
• our inspirational web pages are:
• www.marwickhaulage.com
• www.dorvelcargo.com
• we are open to use stock photos

```html
<!DOCTYPE html>
<html lang="en">
<head>
<meta charset="utf-8">
<title>Heron Freightways LLC</title>
<link href="https://fonts.googleapis.com/css2?family=Open+Sans:ital,wght@0,400;0,600;0,700;1,600&display=swap" rel="stylesheet">
<style>
:root{
  --red:#f04a51;
  --blue:#3277b5;
  --blue-dark:#2a65a0;
  --white:#ffffff;
  --ink:#333740;
  --muted:#7b7f87;
  --panel:#f3f3f3;
  --line:#e2e2e2;
  --footer:#2b2f38;
  --footer-text:#c9ccd2;
}
*{margin:0;padding:0;box-sizing:border-box}
html,body{width:862px;height:1200px;overflow:hidden}
body{font-family:"Open Sans",Arial,sans-serif;color:var(--ink);background:var(--white);position:relative}
.abs{position:absolute}
/* header */
.brand{left:136px;top:14px;font-size:20px;font-weight:700;color:var(--red);letter-spacing:.3px}
.brand-dot{display:inline-block;width:14px;height:14px;border-radius:50%;background:var(--blue);vertical-align:-1px;margin-right:6px}
.btn{top:10px;height:20px;width:82px;background:var(--red);color:var(--white);font-size:8px;font-weight:600;text-align:center;line-height:20px;border-radius:2px}
.btn-login{left:535px}.btn-signup{left:622px}
.search{left:709px;top:10px}
.phone{left:534px;top:37px;font-size:8px;font-weight:700;color:var(--blue);display:flex;align-items:center;gap:4px}
.nav{left:0;top:58px;width:862px;height:31px;background:linear-gradient(var(--blue),var(--blue-dark))}
.nav a{position:absolute;top:10px;font-size:8.5px;color:var(--white);text-decoration:none;text-transform:uppercase}
.hero{left:0;top:89px;width:862px;height:216px;background:linear-gradient(180deg,#e8c79a 0%,#d9a06a 45%,#8a5a34 70%,#5e5a55 100%)}
/* sections */
.section-title{font-size:16px;font-weight:600;color:var(--blue);text-transform:uppercase;border-left:2px solid var(--red);padding-left:8px;line-height:16px}
.about-img{left:134px;top:357px;width:291px;height:145px;background:linear-gradient(135deg,#5e8fc4,#7aa3d2);display:flex;align-items:center;justify-content:center}
.about-img p{width:170px;color:var(--white);font-size:9.5px;font-style:italic;font-weight:600;letter-spacing:.8px;line-height:15px}
.about-text{left:458px;top:384px;width:264px;font-size:7.5px;line-height:13px;color:var(--muted)}
.about-text p+p{margin-top:12px}
.services-band{left:0;top:526px;width:862px;height:371px;background:var(--panel)}
.card{top:587px;width:191px;height:270px;background:var(--white);border:1px solid var(--line)}
.card-photo{height:116px}
.card-bar{margin:12px 0 0 7px;width:18px;height:2px;background:var(--red)}
.card h3{margin:5px 7px 0;font-size:9.5px;font-weight:400;text-transform:uppercase;color:var(--ink)}
.card p{margin:7px 7px 0;font-size:7.5px;line-height:12.8px;color:var(--muted)}
.card .more{position:absolute;right:9px;bottom:6px;font-size:7.5px;color:var(--red);text-transform:uppercase}
.partners{left:306px;top:915px;width:420px;height:82px;border:1px solid var(--line);display:grid;grid-template-columns:135px 148px 1fr;grid-template-rows:1fr 1fr}
.partners div{border-right:1px solid var(--line);border-bottom:1px solid var(--line);display:flex;align-items:center;justify-content:center}
.partners div:nth-child(3n){border-right:none}
.partners div:nth-child(n+4){border-bottom:none}
.badge{width:58px;height:18px;border-radius:3px;background:#cfd1d5}
/* footer */
.footer{left:0;top:1014px;width:862px;height:186px;background:var(--footer);color:var(--footer-text)}
.footer h4{position:absolute;top:25px;font-size:8.5px;font-weight:600;color:#e6e8ec;text-transform:uppercase}
.footer ul{position:absolute;top:49px;list-style:none;font-size:6.5px;font-weight:600;text-transform:uppercase}
.footer li{height:19.3px}
.news-copy{left:135px;top:45px;width:150px;font-size:7.5px;line-height:13.5px}
.email{left:135px;top:97px;width:154px;height:22px;background:#3a404b;font-size:7.5px;font-style:italic;line-height:22px;padding-left:9px}
.email-btn{left:258px;top:97px;width:31px;height:22px;background:var(--blue);display:flex;align-items:center;justify-content:center}
.contact{left:586px;top:37px;font-size:6.8px;font-weight:600;text-transform:uppercase;line-height:19.3px}
.contact b{color:#fff;font-size:7.5px}
.social{left:587px;top:136px;width:16px;height:15px;background:var(--blue)}
.rule{left:135px;top:160px;width:591px;height:1px;background:#444a55}
.copy{left:137px;top:167px;font-size:5.5px;font-weight:600;text-transform:uppercase;color:#7d828c}
</style>
</head>
<body>
<header>
  <div class="abs brand"><span class="brand-dot"></span>Heron Freightways</div>
  <div class="abs btn btn-login">LOGIN</div>
  <div class="abs btn btn-signup">SIGN UP</div>
  <svg class="abs search" width="16" height="16" viewBox="0 0 16 16"><circle cx="6.5" cy="6.5" r="5" fill="none" stroke="#3277b5" stroke-width="1.6"/><line x1="10.2" y1="10.2" x2="15" y2="15" stroke="#3277b5" stroke-width="1.8"/></svg>
  <div class="abs phone"><svg width="9" height="9" viewBox="0 0 10 10"><path d="M2 1l2 2-1 1.5c.7 1.3 1.5 2.1 2.8 2.8L7.3 6l2 2-1.3 1.5C4.5 9 1 5.5.5 2.3z" fill="#3277b5"/></svg>1 - 800- 555- 0142 OR (555) 010-3388</div>
  <nav class="abs nav">
    <a style="left:135px">Home</a><a style="left:194px">About Us</a><a style="left:270px">Solutions</a><a style="left:351px">Expertise</a><a style="left:428px">Investors</a><a style="left:507px">Careers</a><a style="left:577px">Contact</a>
  </nav>
</header>
<div class="abs hero" role="img" aria-label="Refrigerated truck with company livery driving along a highway at sunset"></div>

<section>
  <h2 class="abs section-title" style="left:375px;top:325px">About Us</h2>
  <div class="abs about-img" role="img" aria-label="Blue-tinted photo of shoppers carrying bags"><p>“We carry and deliver almost any type of temperature sensitive products anywhere in the United States.”</p></div>
  <div class="abs about-text">
    <p>Heron Freightways LLC currently has the very latest in transport refrigeration technology. Our brand new trucks and professional looking equipment set the standard with outstanding efficiency and reliability paired with superior temperature control.</p>
    <p>We offer quality and reliability. We’ve got you and your business covered day and night, from origin to destination.</p>
  </div>
</section>

<section>
  <div class="abs services-band"></div>
  <h2 class="abs section-title" style="left:363px;top:552px">Our Services</h2>
  <article class="abs card" style="left:135px">
    <div class="card-photo" role="img" aria-label="Blue and white truck on a highway" style="background:linear-gradient(135deg,#3f6fb8,#9bb3cf)"></div>
    <div class="card-bar"></div><h3>Supply Chain Manangement</h3>
    <p>Single-origin coffee small batch PBR&amp;B pork belly +1. VHS mlkshk hashtag +1. Humble-brag pitchfork hella small batch godard, bushwick blog irony put a bird on it keffiyeh migas church-key PBR&amp;B. ut a bird on it gastropub 3 wolf moon blog, meditation try-hard yr occupy fanny pack waistcoat health goth fashion axe.</p>
    <span class="more">Read More</span>
  </article>
  <article class="abs card" style="left:335px">
    <div class="card-photo" role="img" aria-label="Truck driver standing beside a white truck" style="background:linear-gradient(135deg,#a9bdd3,#5d6f82)"></div>
    <div class="card-bar"></div><h3>Refrigeration Specialists</h3>
    <p>Single-origin coffee small batch PBR&amp;B pork belly +1. VHS mlkshk hashtag +1. Humble-brag pitchfork hella small batch godard, bushwick blog irony put a bird on it keffiyeh migas church-key PBR&amp;B. ut a bird on it gastropub 3 wolf moon blog, meditation try-hard yr occupy fanny pack waistcoat health goth fashion axe.</p>
    <span class="more">Read More</span>
  </article>
  <article class="abs card" style="left:535px">
    <div class="card-photo" role="img" aria-label="Red truck hauling a trailer at dusk" style="background:linear-gradient(135deg,#c9aa8f,#7a4a46)"></div>
    <div class="card-bar"></div><h3>Across USA &amp; Cananda</h3>
    <p>Single-origin coffee small batch PBR&amp;B pork belly +1. VHS mlkshk hashtag +1. Humble-brag pitchfork hella small batch godard, bushwick blog irony put a bird on it keffiyeh migas church-key PBR&amp;B. ut a bird on it gastropub 3 wolf moon blog, meditation try-hard yr occupy fanny pack waistcoat health goth fashion axe.</p>
    <span class="more">Read More</span>
  </article>
</section>

<section>
  <h2 class="abs section-title" style="left:135px;top:918px;color:#6d7179;border-left-color:#6d7179">Our Partners</h2>
  <div class="abs partners">
    <div><span class="badge"></span></div><div><span class="badge"></span></div><div><span class="badge"></span></div>
    <div><span class="badge"></span></div><div><span class="badge"></span></div><div><span class="badge"></span></div>
  </div>
</section>

<footer class="abs footer">
  <h4 style="left:135px">Newsletter Subscribe</h4>
  <p class="abs news-copy">Subscribe to our newsletter and we will inform you about projects and developements.</p>
  <div class="abs email">Your Email ....</div>
  <div class="abs email-btn"><svg width="11" height="8" viewBox="0 0 11 8"><rect x=".5" y=".5" width="10" height="7" fill="none" stroke="#fff"/><path d="M.5 .5l5 4 5-4" fill="none" stroke="#fff"/></svg></div>
  <h4 style="left:320px">Quick Links</h4>
  <ul style="left:320px"><li>&gt; About Us</li><li>&gt; Company History</li><li>&gt;Company Events</li><li>&gt; Distributions</li><li>&gt; How We Work</li></ul>
  <h4 style="left:442px">Industry News</h4>
  <ul style="left:442px"><li>&gt; Transportation</li><li>&gt; Refridgeration Standards</li><li>&gt; Rail Freight</li><li>&gt; Air Freight</li><li>&gt; Large Projects</li></ul>
  <h4 style="left:585px">Contact Us</h4>
  <div class="abs contact">4100 Mesquite Rd. Alton Ridge, TX 78000<br><b>Toll Free: 1-800-555-0142</b><br><b>Local Number: (555) 010-3388</b><br>dispatch@heronfreightways.net<br>Info@heronfreightways.net</div>
  <div class="abs social" aria-label="Chatterbook"></div>
  <div class="abs rule"></div>
  <div class="abs copy">Heron Freightways 2016, All Rights Reserved</div>
</footer>
</body>
</html>
```